Calder Pizza - Takeout Menu Design

We are looking for a takeout menu design.
We are looking for a( 5" x 8.5" DOUBLE SIDED) flyer with our available pizza flavors
Must be easy to ready and not "busy"

Must include our logo (attached)
website: www.calderpizza.ca
address:
Fenwick Ridge Plaza
417, 318 9 Avenue SW
and the following details:
Visit our website for our complete appetizer, pasta, salad and catering menu.

Winner of this contest will also be offered to create a few print designs via printhive.

Please do not hesitate to ask any questions.

Target Market(s)

Business / Office clientele

Industry/Entity Type

Pizza place / specializing in corporate orders

Requirements
Must have
• Easy to read
Should not have
• Can not be busy or cluttered

```html
<!DOCTYPE html>
<html lang="en">
<head>
<meta charset="utf-8">
<title>Calder Pizza – Takeout Menu</title>
<link href="https://fonts.googleapis.com/css2?family=Nunito:ital,wght@0,400;0,600;0,700;0,800;1,400;1,600&display=swap" rel="stylesheet">
<style>
  :root {
    --red: #c8311f;
    --ink: #141414;
    --paper: #efedee;
    --bg: #ffffff;
    --tint: #f3d9d4;
  }
  * { box-sizing: border-box; margin: 0; padding: 0; }
  html, body { width: 1200px; height: 848px; overflow: hidden; background: var(--bg); }
  body { position: relative; font-family: "Nunito", sans-serif; color: var(--ink); }

  .page {
    position: absolute; top: 33px; width: 469px; height: 789px;
    background: var(--paper); overflow: hidden;
    box-shadow: 4px 6px 10px rgba(0,0,0,.25);
  }
  .page--front { left: 104px; }
  .page--back { left: 637px; }

  .brand {
    position: absolute; top: 44px; left: 0; width: 100%;
    text-align: center; font-size: 44px; font-weight: 400; letter-spacing: 1px;
    color: var(--ink); line-height: 1; text-transform: uppercase;
  }
  .tagline {
    position: absolute; top: 128px; left: 0; width: 100%;
    text-align: center; font-style: italic; font-size: 17.5px; line-height: 22px;
  }

  .banner {
    position: absolute; left: 8px; height: 35px; background: var(--red);
    color: #fff; font-weight: 700; font-size: 16px; letter-spacing: .3px;
    display: flex; align-items: center; padding-left: 26px;
    clip-path: polygon(0 0, 100% 0, 96% 50%, 100% 100%, 0 100%, 5% 50%);
  }
  .size {
    position: absolute; width: 37px; height: 37px; border-radius: 50%;
    background: #000; color: #fff; font-weight: 700; font-size: 16px;
    display: flex; align-items: center; justify-content: center;
  }

  .row {
    position: absolute; display: flex; align-items: baseline;
    font-size: 12.5px; line-height: 15px;
  }
  .page--front .row { left: 13px; width: 418px; }
  .page--back .row { left: 20px; width: 427px; }
  .row::before { content: "•"; color: var(--ink); margin-right: 3px; font-size: 11px; }
  .name { color: var(--red); font-size: 13px; white-space: nowrap; }
  .leader { flex: 1; border-bottom: 1.5px dotted var(--ink); margin: 0 2px 0 4px; transform: translateY(-3px); }
  .p8 { width: 62px; padding-left: 3px; font-size: 11.5px; }
  .p13 { width: 44px; font-size: 11.5px; }
  .page--back .p8 { width: 66px; }
  .desc {
    position: absolute; font-size: 10px; line-height: 12.2px; color: var(--ink);
  }
  .page--front .desc { left: 22px; }
  .page--back .desc { left: 30px; }

  .visit {
    position: absolute; left: 29px; top: 596px;
    font-style: italic; font-size: 15px; line-height: 19px;
  }
  .web { position: absolute; left: 29px; top: 656px; color: var(--red); font-weight: 800; font-size: 19px; letter-spacing: .4px; }
  .address { position: absolute; left: 29px; top: 687px; font-size: 13.5px; line-height: 17px; }

  .art-pizza {
    position: absolute; left: 274px; top: 515px; width: 304px; height: 304px; border-radius: 50%;
    background: radial-gradient(circle, #f6e3df 0%, #efc9c1 70%, #e3a89c 100%);
  }
  .art-peppers {
    position: absolute; left: 20px; top: 12px; width: 70px; height: 70px; border-radius: 40%;
    background: radial-gradient(circle, #f2d3cd, rgba(239,237,238,0));
  }
  .art-basil {
    position: absolute; left: 400px; top: 716px; width: 60px; height: 66px; border-radius: 45%;
    background: radial-gradient(circle, #f0cfc8, rgba(239,237,238,0));
  }
</style>
</head>
<body>

<section class="page page--front">
  <div class="brand">Calder Pizza</div>
  <p class="tagline">All of our pizzas are prepared fresh everyday using<br>only the finest mozzarella blend and ingredients.</p>

  <div class="banner" style="top:212px;width:252px;">CLASSIC TAKE-OUT PIZZA</div>
  <div class="size" style="top:210px;left:325px;">8"</div>
  <div class="size" style="top:210px;left:386px;">13"</div>

  <div class="row" style="top:258px"><span class="name">Pepperoni &amp; Mushroom</span><span class="leader"></span><span class="p8">$12.99</span><span class="p13">$30.95</span></div>
  <div class="row" style="top:274px"><span class="name">Pepperoni</span><span class="leader"></span><span class="p8">$11.99</span><span class="p13">$29.95</span></div>
  <div class="row" style="top:289px"><span class="name">Hawaiian</span><span class="leader"></span><span class="p8">$12.99</span><span class="p13">$30.95</span></div>
  <div class="row" style="top:305px"><span class="name">Beef &amp; Mushroom</span><span class="leader"></span><span class="p8">$13.49</span><span class="p13">$32.95</span></div>
  <div class="row" style="top:320px"><span class="name">Pepperoni &amp; Ham</span><span class="leader"></span><span class="p8">$12.99</span><span class="p13">$30.95</span></div>
  <div class="row" style="top:336px"><span class="name">Ham &amp; Mushroom</span><span class="leader"></span><span class="p8">$12.99</span><span class="p13">$30.95</span></div>
  <div class="row" style="top:351px"><span class="name">Beef &amp; Onion</span><span class="leader"></span><span class="p8">$13.49</span><span class="p13">$32.95</span></div>
  <div class="row" style="top:367px"><span class="name">Cheese</span><span class="leader"></span><span class="p8">$11.99</span><span class="p13">$29.95</span></div>

  <div class="banner" style="top:401px;width:266px;">SPECIALTY TAKE-OUT PIZZA</div>
  <div class="size" style="top:400px;left:325px;">8"</div>
  <div class="size" style="top:400px;left:386px;">13"</div>

  <div class="row" style="top:445px"><span class="name">All Meat</span><span class="leader"></span><span class="p8">$13.99</span><span class="p13">$33.95</span></div>
  <p class="desc" style="top:460px">Pepperoni, Beef &amp; Smoked Ham</p>
  <div class="row" style="top:478px"><span class="name">Meat Supreme</span><span class="leader"></span><span class="p8">$14.99</span><span class="p13">$35.95</span></div>
  <p class="desc" style="top:493px">Pepperoni, Beef, Salami, Smoked Ham &amp; Bacon</p>
  <div class="row" style="top:511px"><span class="name">BBQ Chicken</span><span class="leader"></span><span class="p8">$13.99</span><span class="p13">$33.95</span></div>
  <p class="desc" style="top:526px">Chicken Breast, Hickory BBQ Sauce &amp; Red Onions</p>
  <div class="row" style="top:544px"><span class="name">Spicy BBQ Chicken</span><span class="leader"></span><span class="p8">$14.49</span><span class="p13">$35.95</span></div>
  <p class="desc" style="top:559px">Chicken Breast, Hickory BBQ Sauce, Red Onions<br>&amp; Banana Peppers</p>
  <div class="row" style="top:589px"><span class="name">Deluxe</span><span class="leader"></span><span class="p8">$14.49</span><span class="p13">$34.95</span></div>
  <p class="desc" style="top:604px">Pepperoni, Mushrooms, Ham, Tomatoes, Green Peppers<br>and Red Onions</p>
  <div class="row" style="top:635px"><span class="name">Double Pepperoni</span><span class="leader"></span><span class="p8">$13.49</span><span class="p13">$32.95</span></div>
  <p class="desc" style="top:650px">Loads of Pepperoni</p>
  <div class="row" style="top:668px"><span class="name">Four Cheese</span><span class="leader"></span><span class="p8">$13.49</span><span class="p13">$32.95</span></div>
  <p class="desc" style="top:683px">Mozzarella, Feta, Romano and Cheddar Cheese</p>
  <div class="row" style="top:701px"><span class="name">Greek</span><span class="leader"></span><span class="p8">$13.99</span><span class="p13">$33.95</span></div>
  <p class="desc" style="top:716px">Feta Cheese, Tomato, Green Peppers, Red Onions<br>and Black Olives</p>

  <div class="art-basil" role="img" aria-label="Line drawing of basil leaves"></div>
</section>

<section class="page page--back">
  <div class="art-peppers" role="img" aria-label="Line drawing of chili peppers"></div>
  <div class="size" style="top:54px;left:332px;">8"</div>
  <div class="size" style="top:54px;left:393px;">13"</div>

  <div class="row" style="top:99px"><span class="name">Greek Supreme</span><span class="leader"></span><span class="p8">$14.99</span><span class="p13">$35.95</span></div>
  <p class="desc" style="top:114px">Chicken Breast, Feta Cheese, Tomato, Green Pepper,<br>Red Onions &amp; Black Olives</p>
  <div class="row" style="top:139px"><span class="name">Mediterranean Chicken</span><span class="leader"></span><span class="p8">$14.79</span><span class="p13">$35.95</span></div>
  <p class="desc" style="top:154px">Seasoned Chicken Breast, Tomatoes, Red Onions<br>and Feta Cheese</p>
  <div class="row" style="top:180px"><span class="name">Montreal</span><span class="leader"></span><span class="p8">$13.49</span><span class="p13">$32.95</span></div>
  <p class="desc" style="top:195px">Pepperoni &amp; Double Smoked Bacon</p>
  <div class="row" style="top:207px"><span class="name">Athenean</span><span class="leader"></span><span class="p8">$14.49</span><span class="p13">$34.95</span></div>
  <p class="desc" style="top:222px">Chicken Breast, Spinach, Feta Cheese and Tomato</p>
  <div class="row" style="top:235px"><span class="name">Supreme</span><span class="leader"></span><span class="p8">$13.49</span><span class="p13">$32.95</span></div>
  <p class="desc" style="top:250px">Pepperoni, Mushrooms &amp; Green Peppers</p>
  <div class="row" style="top:263px"><span class="name">Canadian</span><span class="leader"></span><span class="p8">$13.49</span><span class="p13">$32.95</span></div>
  <p class="desc" style="top:278px">Pepperoni, Mushrooms &amp; Ham</p>
  <div class="row" style="top:291px"><span class="name">Original Spinach</span><span class="leader"></span><span class="p8">$13.49</span><span class="p13">$32.95</span></div>
  <p class="desc" style="top:306px">Spinach &amp; Feta Cheese</p>
  <div class="row" style="top:319px"><span class="name">Chicken Club</span><span class="leader"></span><span class="p8">$14.79</span><span class="p13">$35.95</span></div>
  <p class="desc" style="top:334px">Chicken Breast, Double Smoked Bacon, Red Onions<br>and Tomatoes</p>
  <div class="row" style="top:359px"><span class="name">Zeus</span><span class="leader"></span><span class="p8">$13.95</span><span class="p13">$33.95</span></div>
  <p class="desc" style="top:374px">Spinach, Feta Cheese and Tomatoes</p>
  <div class="row" style="top:387px"><span class="name">Vegetarian</span><span class="leader"></span><span class="p8">$13.49</span><span class="p13">$32.95</span></div>
  <p class="desc" style="top:402px">Mushrooms, Tomatoes, Green Peppers<br>and Black Olives</p>
  <div class="row" style="top:427px"><span class="name">Calder Special</span><span class="leader"></span><span class="p8">$14.49</span><span class="p13">$34.95</span></div>
  <p class="desc" style="top:442px">Pepperoni, Mushrooms, Ham, Green Peppers<br>and Black Olives</p>

  <div class="art-pizza" role="img" aria-label="Line drawing of a sliced pizza with tomato and pepper toppings"></div>

  <p class="visit">Visit our website for<br>our complete appetizer,<br>pasta, salad and catering menu</p>
  <p class="web">www.calderpizza.ca</p>
  <p class="address">Fenwick Ridge Plaza<br>417, 318 9 Avenue SW</p>
</section>

</body>
</html>
```